Business Card Design needed for logo design project

This project is linked to Dental Clinic Logo (SEE ATTACHED LOGO FOR GUIDANCE).

Our company needs a Business Card Design. Please refer to our original project in the link above.

Industry/Entity Type

Business

```html
<!DOCTYPE html>
<html lang="en">
<head>
<meta charset="utf-8">
<title>Harrowgate Dental Clinic – Business Card</title>
<link href="https://fonts.googleapis.com/css2?family=Open+Sans:wght@400;600;700&family=Raleway:wght@400;500&display=swap" rel="stylesheet">
<style>
  :root {
    --page: #e9ecec;
    --night: #1b1d1f;
    --royal: #1447d8;
    --sky: #33b6e6;
    --mark: #1a2fe0;
    --ink: #4a4f55;
    --ink-soft: #6c7278;
    --paper: #ffffff;
  }
  * { margin: 0; padding: 0; box-sizing: border-box; }
  html, body { width: 872px; height: 1200px; overflow: hidden; }
  body { position: relative; background: var(--page); font-family: "Open Sans", sans-serif; }

  .card { position: absolute; left: 146px; width: 585px; overflow: hidden; box-shadow: 0 1px 4px rgba(0,0,0,.18); }

  .card--front {
    top: 109px; height: 333px;
    background:
      linear-gradient(125deg, transparent 30%, rgba(255,255,255,.18) 48%, transparent 62%),
      radial-gradient(ellipse at 55% 55%, var(--sky) 0%, #2a8fe4 45%, var(--royal) 100%);
  }
  .card--back { top: 507px; height: 334px; background: var(--paper); }

  .brand { position: absolute; display: flex; align-items: center; }
  .brand__dot { border-radius: 50%; background: var(--mark); flex: none; }
  .brand__name { font-weight: 700; line-height: 1.05; }
  .brand__name span { display: block; }

  .card--front .brand { left: 158px; top: 110px; }
  .card--front .brand__dot { width: 114px; height: 114px; margin-right: 22px; }
  .card--front .brand__name { color: var(--paper); }
  .card--front .brand__name .sm { font-size: 15px; }
  .card--front .brand__name .lg { font-size: 29px; }
  .card--front .brand__name .md { font-size: 19px; }

  .card--back .brand { left: 43px; top: 26px; }
  .card--back .brand__dot { width: 85px; height: 85px; margin-right: 15px; }
  .card--back .brand__name { color: var(--ink); }
  .card--back .brand__name .sm { font-size: 12px; }
  .card--back .brand__name .lg { font-size: 23px; }
  .card--back .brand__name .md { font-size: 15px; }

  .contact { position: absolute; left: 45px; font-family: "Raleway", sans-serif; font-size: 13.5px; color: var(--ink); }
  .contact li { list-style: none; display: flex; align-items: center; height: 24px; }
  .contact svg { width: 18px; height: 16px; margin-right: 18px; flex: none; }
  .contact--lines { top: 133px; }
  .contact--address { top: 236px; align-items: flex-start; }
  .contact--address li { height: auto; line-height: 19px; }

  .person { position: absolute; right: 31px; top: 128px; text-align: right; }
  .person__name { font-size: 25px; font-weight: 600; color: var(--mark); line-height: 1.1; }
  .person__role { font-family: "Raleway", sans-serif; font-size: 12.5px; color: var(--ink-soft); }

  .swoosh { position: absolute; left: 0; bottom: 0; width: 585px; height: 80px; }

  .standalone { position: absolute; left: 347px; display: flex; align-items: center; }
  .standalone .brand__dot { width: 70px; height: 70px; margin-right: 12px; }
  .standalone .brand__name .sm { font-size: 10px; }
  .standalone .brand__name .lg { font-size: 19px; }
  .standalone .brand__name .md { font-size: 12px; }
  .standalone--light { top: 937px; }
  .standalone--light .brand__name { color: var(--ink-soft); }
  .standalone--dark { top: 1087px; }
  .standalone--dark .brand__name { color: #555b61; }

  .night-band { position: absolute; left: 0; top: 1050px; width: 872px; height: 150px; background: var(--night); }
</style>
</head>
<body>

<section class="card card--front">
  <div class="brand">
    <div class="brand__dot"></div>
    <div class="brand__name"><span class="sm">The</span><span class="lg">Harrowgate</span><span class="md">Dental Clinic</span></div>
  </div>
</section>

<section class="card card--back">
  <div class="brand">
    <div class="brand__dot"></div>
    <div class="brand__name"><span class="sm">The</span><span class="lg">Harrowgate</span><span class="md">Dental Clinic</span></div>
  </div>

  <ul class="contact contact--lines">
    <li><svg viewBox="0 0 18 16"><rect x="1.5" y="3" width="15" height="10" fill="none" stroke="#1a2fe0" stroke-width="1.3"/><path d="M1.5 3 L9 9 L16.5 3" fill="none" stroke="#1a2fe0" stroke-width="1.3"/></svg>m.santos@harrowgatedental.ph</li>
    <li><svg viewBox="0 0 18 16"><rect x="5" y="1" width="8" height="14" rx="1" fill="none" stroke="#1a2fe0" stroke-width="1.4"/><rect x="6.5" y="3" width="5" height="4" fill="#1a2fe0"/></svg>(+63) 900-555-0142</li>
    <li><svg viewBox="0 0 18 16"><rect x="5" y="1" width="8" height="14" rx="1" fill="none" stroke="#1a2fe0" stroke-width="1.4"/><rect x="6.5" y="3" width="5" height="4" fill="#1a2fe0"/></svg>(+63) 900-555-0143</li>
  </ul>

  <ul class="contact contact--address">
    <li><svg viewBox="0 0 18 16"><path d="M9 15 C5 10 4 8 4 6 A5 5 0 0 1 14 6 C14 8 13 10 9 15 Z" fill="#1a2fe0"/><circle cx="9" cy="6" r="1.8" fill="#fff"/></svg><span>Lumen Ave., Riverside East, Maravilla City<br>Verano, Philippines 3400</span></li>
  </ul>

  <div class="person">
    <p class="person__name">Marco Reyes Santos</p>
    <p class="person__role">Marketing Manager</p>
  </div>

  <svg class="swoosh" viewBox="0 0 585 80" preserveAspectRatio="none">
    <defs>
      <linearGradient id="swooshFill" x1="0" y1="0" x2="1" y2="0">
        <stop offset="0" stop-color="#1f63dc"/>
        <stop offset="0.5" stop-color="#35b3e8"/>
        <stop offset="1" stop-color="#1447d8"/>
      </linearGradient>
    </defs>
    <path d="M0 26 C160 40 380 38 585 0 L585 80 L0 80 Z" fill="url(#swooshFill)"/>
    <path d="M40 32 C120 38 170 40 220 41" fill="none" stroke="#fff" stroke-width="3" stroke-linecap="round"/>
  </svg>
</section>

<div class="brand standalone standalone--light">
  <div class="brand__dot"></div>
  <div class="brand__name"><span class="sm">The</span><span class="lg">Harrowgate</span><span class="md">Dental Clinic</span></div>
</div>

<div class="night-band"></div>

<div class="brand standalone standalone--dark">
  <div class="brand__dot"></div>
  <div class="brand__name"><span class="sm">The</span><span class="lg">Harrowgate</span><span class="md">Dental Clinic</span></div>
</div>

</body>
</html>
```